International Property Consultancy

Detailed Wireframe and info document attached.

Brief Overview:

I need a dynamic and well designed website that is easy to use and understand. It has to be unique and different to generic templates that most websites seem to be these days. PLEASE NO GENERIC TEMPLATES FROM THE INTERNET.

Our business has 10 years experience working on struggling international developments that we then work in-house for to turn around and brings bout success. We stay within a project often for long periods of time until success is achieved. We are unique in our approach and completely different to the standard routes to market for many developments. The site is for developers to see what we have done in regards to previous projects, as such we want to incorporate video into this site with a strong design aesthetic. There will be videos of the past projects we have worked on, which will act as case studies.

I like very simple but punchy websites, that people can navigate and understand very easily. Also a big fan of unique and well thought out design aesthetic.

Initial Site layout thoughts:

1) Homepage:
2) About Us
3) What we've done / Work
This part has the projects we have worked on (France, Portugal, London, Morocco). Each one will have some video content and photo images, but also would be good to have a succinct way to mention what we did and the successes in a clever and punchy way.

4) Contact Us

* This is just a guideline. Would be open to input and creative direction on your own part.

*More details and websites we like can be seen in the brief doc attached.

PLEASE VIEW THE WIREFRAME WORD DOC ATTACHED.

Here there are also some more examples to help:

Here are just a few examples of websites and what I like about them:

- www.velmorit.com (clean, nice geometric design aesthetic, good animation when loading and changing pages well thought out all though also coulee be considered a bit dull and basic after the initial homepage slide)
- https://www.farbridgeloop.net (Clean site, quite clinical, lacks video content and doesn't engage greatly).
- https://quiltmarsh.com (minimal, and like how it mixes the design aesthetic more with video and photo content)

- https://www.theamberotter.com (like the layout of this and how it displays the projects and work section)

- https://drov.com (Good use of video content)

- https://crafthalo.studio (minimal to the point and mixes design with video and animation etc...)

Here is another couple of cool websites that may help give you some direction: https://tidewellgroup.com www.drov.com

Hi there, One of the things I thought would be good on the homepage is to add the logo with a 'digital landscape' before flicking down into a slide with video content of the projects... Just an idea but have posted some pics in the brief. We would get this animated for the site. But if you have better ideas, please do run with them. Thanks,

Target Market(s)

Property developers

Number of Pages Required

4 page

Font styles to use
Other font styles liked:
• Read brief

Requirements
Must have
• Needs to be clean, dynamic and easy to follow on desktop and mobile. We will use it as a kind of portfolio website so will need to embed video of past projects we have worked on.

Read brief in docs.
Nice to have
• Clean
Should not have
• Not be another generic template website.
Not have random property stock photos. (We are not a property agency).

```html
<!DOCTYPE html>
<html lang="en">
<head>
<meta charset="utf-8">
<title>Calvessa — International Property Developments</title>
<link href="https://fonts.googleapis.com/css2?family=Nunito+Sans:wght@400;600;700;800&display=swap" rel="stylesheet">
<style>
  :root {
    --ink: #04111a;
    --night: #030f16;
    --white: #ffffff;
    --accent: #1d8fc0;
    --mist: #d6eff8;
    --mist-soft: #eaf7fc;
    --grey-text: #2b2f33;
    --muted: #c9d1d6;
  }
  * { margin: 0; padding: 0; box-sizing: border-box; }
  html, body { width: 1200px; height: 3125px; overflow: hidden; }
  body {
    font-family: "Nunito Sans", "Helvetica Neue", Arial, sans-serif;
    color: var(--ink);
    background: var(--white);
    position: relative;
  }
  a { color: inherit; }
  .section { position: absolute; left: 0; width: 1200px; overflow: hidden; }
  .section--light { background: var(--white); color: var(--ink); }
  .section--dark { background: var(--night); color: var(--white); }

  .site-nav { position: absolute; left: 0; width: 1200px; height: 40px; }
  .brand {
    position: absolute; left: 215px; top: 0;
    font-size: 29px; font-weight: 600; letter-spacing: -0.5px; line-height: 40px;
  }
  .nav-links {
    position: absolute; right: 217px; top: 0; display: flex; gap: 17px;
    list-style: none; font-size: 12.5px; font-weight: 600; line-height: 40px;
  }
  .nav-links a { text-decoration: none; }
  .nav-links .is-active { color: var(--accent); border-bottom: 1.5px solid var(--accent); padding-bottom: 3px; }

  /* Hero */
  .hero { top: 0; height: 754px; }
  .hero .site-nav { top: 26px; }
  .hero-title { position: absolute; left: 216px; top: 142px; font-size: 44px; font-weight: 600; letter-spacing: -0.3px; }
  .hero-sub { position: absolute; left: 216px; top: 203px; font-size: 25.5px; font-weight: 400; color: var(--grey-text); }
  .landscape {
    position: absolute; left: 0; top: 267px; width: 1200px; height: 487px;
    background: linear-gradient(180deg, var(--white) 0%, var(--mist-soft) 22%, var(--mist) 60%, var(--mist-soft) 100%);
  }
  .hero-brand {
    position: absolute; left: 0; width: 1200px; top: 416px; text-align: center;
    font-size: 78px; font-weight: 700; letter-spacing: -1px; line-height: 90px;
  }
  .play-button { position: absolute; left: 564px; top: 517px; }
  .scroll-cue { position: absolute; left: 948px; top: 572px; }

  /* Work */
  .work { top: 754px; height: 754px; }
  .work .site-nav { top: 29px; }
  .work-intro { position: absolute; left: 214px; top: 145px; width: 720px; font-size: 19.5px; line-height: 27px; }
  .text-link { position: absolute; font-size: 16px; font-weight: 600; color: var(--accent); text-decoration: underline; text-underline-offset: 3px; }
  .work .text-link { left: 214px; top: 220px; }
  .project-slide { position: absolute; top: 302px; height: 340px; }
  .slide--prev { left: 0; width: 121px; background: linear-gradient(180deg, #9fb4c2 0%, #6e8596 55%, #4a5b64 100%); }
  .slide--current { left: 239px; width: 721px; background: linear-gradient(180deg, #3f5475 0%, #7e7fa3 40%, #d3b2b7 70%, #4b4a5e 100%); }
  .slide--next { left: 1081px; width: 119px; background: linear-gradient(180deg, #c7a9b6 0%, #9a7c7a 35%, #4f6a2f 65%, #2f4a1d 100%); }
  .slide-label { position: absolute; top: 440px; font-size: 44px; font-weight: 700; line-height: 60px; color: var(--white); }
  .label--current { left: 214px; }
  .label--next { left: 1048px; white-space: nowrap; }
  .slider-arrow { position: absolute; top: 685px; }

  /* About */
  .about { top: 1508px; height: 955px; }
  .about .site-nav { top: 34px; }
  .about-copy { position: absolute; left: 215px; top: 139px; width: 525px; font-size: 19.5px; line-height: 27px; color: var(--grey-text); }
  .about-copy p + p { margin-top: 27px; }
  .about .text-link { left: 215px; top: 400px; }
  .stat { position: absolute; left: 884px; }
  .stat-value { font-size: 56px; font-weight: 800; line-height: 60px; letter-spacing: -1px; }
  .stat-label { font-size: 16.5px; line-height: 22px; color: var(--grey-text); margin-left: 2px; }
  .stat--members { top: 136px; }
  .stat--years { top: 275px; }
  .photo { position: absolute; }
  .photo--team { left: 0; top: 490px; width: 163px; height: 365px; background: linear-gradient(135deg, #c9c4bf 0%, #8a6a55 50%, #3b3a4a 100%); }
  .photo--towers { left: 237px; top: 522px; width: 319px; height: 309px; background: linear-gradient(180deg, #d7e0e8 0%, #55606b 55%, #1e2630 100%); }
  .photo--workshop { left: 637px; top: 462px; width: 319px; height: 410px; background: linear-gradient(180deg, #9a6a4a 0%, #6b5a50 45%, #3a3a3e 100%); }
  .photo--desk { left: 1026px; top: 511px; width: 174px; height: 331px; background: linear-gradient(135deg, #8fbfbf 0%, #d6e3e0 50%, #2b4a52 100%); }

  /* Contact */
  .contact { top: 2463px; height: 662px; }
  .contact .site-nav { top: 30px; }
  .contact-title { position: absolute; left: 213px; top: 210px; font-size: 42px; font-weight: 700; letter-spacing: -0.5px; }
  .contact-email { position: absolute; left: 214px; top: 275px; font-size: 17px; color: var(--muted); text-underline-offset: 3px; }
  .contact-pitch { position: absolute; left: 605px; top: 215px; width: 400px; font-size: 27px; line-height: 31px; }
  .contact-note { position: absolute; left: 605px; top: 310px; font-size: 16.5px; color: var(--muted); }
  .contact .text-link { left: 606px; top: 358px; }
  .footer-legal { position: absolute; left: 216px; top: 540px; font-size: 10.5px; color: var(--muted); }
  .footer-legal a { margin-left: 4px; text-decoration: underline; }
  .social-list {
    position: absolute; right: 217px; top: 536px; display: flex; gap: 16px;
    list-style: none; font-size: 12.5px; font-weight: 700; color: var(--white);
  }
  .social-list a { text-decoration: none; }
</style>
</head>
<body>

<section class="section section--light hero">
  <div class="landscape" role="img" aria-label="Light blue wireframe digital landscape of rolling hills"></div>
  <nav class="site-nav">
    <span class="brand">calvessa.</span>
    <ul class="nav-links">
      <li><a class="is-active" href="#">Home</a></li>
      <li><a href="#">Work</a></li>
      <li><a href="#">About</a></li>
      <li><a href="#">Contact</a></li>
    </ul>
  </nav>
  <h1 class="hero-title">We are Calvessa</h1>
  <p class="hero-sub">We fulfill international property developments</p>
  <div class="hero-brand">calvessa.</div>
  <svg class="play-button" width="72" height="72" viewBox="0 0 72 72" aria-label="Play video">
    <circle cx="36" cy="36" r="35" fill="#1f4a5a" opacity="0.45"/>
    <circle cx="36" cy="36" r="26" fill="#0d3645"/>
    <path d="M30 25 L48 36 L30 47 Z" fill="#ffffff"/>
  </svg>
  <svg class="scroll-cue" width="24" height="124" viewBox="0 0 24 124">
    <text x="0" y="0" transform="translate(16 52) rotate(-90)" font-family="Nunito Sans, sans-serif" font-size="10" font-weight="800" letter-spacing="1.5" fill="#04111a">SCROLL</text>
    <line x1="12" y1="60" x2="12" y2="120" stroke="#04111a" stroke-width="1"/>
    <path d="M7 115 L12 121 L17 115" fill="none" stroke="#04111a" stroke-width="1"/>
  </svg>
</section>

<section class="section section--dark work">
  <nav class="site-nav">
    <span class="brand">calvessa.</span>
    <ul class="nav-links">
      <li><a href="#">Home</a></li>
      <li><a class="is-active" href="#">Work</a></li>
      <li><a href="#">About</a></li>
      <li><a href="#">Contact</a></li>
    </ul>
  </nav>
  <p class="work-intro">We deliver a unique and truly bespoke approach to delivering international developments to market, with over 10 years success around the world.</p>
  <a class="text-link" href="#">See our work</a>
  <div class="project-slide slide--prev" role="img" aria-label="London project: bridge over the river"></div>
  <div class="project-slide slide--current" role="img" aria-label="France project: Paris skyline at dusk"></div>
  <div class="project-slide slide--next" role="img" aria-label="Morocco project: mountains and palm groves"></div>
  <span class="slide-label label--current">France</span>
  <span class="slide-label label--next">Morocco</span>
  <svg class="slider-arrow" style="left:244px" width="24" height="14" viewBox="0 0 24 14" aria-label="Previous">
    <path d="M23 7 H2 M8 1 L2 7 L8 13" fill="none" stroke="#fff" stroke-width="1.6"/>
  </svg>
  <svg class="slider-arrow" style="left:925px" width="24" height="14" viewBox="0 0 24 14" aria-label="Next">
    <path d="M1 7 H22 M16 1 L22 7 L16 13" fill="none" stroke="#fff" stroke-width="1.6"/>
  </svg>
</section>

<section class="section section--light about">
  <nav class="site-nav">
    <span class="brand">calvessa.</span>
    <ul class="nav-links">
      <li><a href="#">Home</a></li>
      <li><a href="#">Work</a></li>
      <li><a class="is-active" href="#">About</a></li>
      <li><a href="#">Contact</a></li>
    </ul>
  </nav>
  <div class="about-copy">
    <p>We fulfill international property developments in a truly unique way. We’ve worked on projects around the world taking developments from fields to award wining resorts, and tired underachieving developments to overachieving goliaths.</p>
    <p>By creating a unique and bespoke in-house white-label strategy that allows each project to be the only beneficiary of the work we do.</p>
  </div>
  <a class="text-link" href="#">About Calvessa</a>
  <div class="stat stat--members">
    <div class="stat-value">30+</div>
    <div class="stat-label">Members</div>
  </div>
  <div class="stat stat--years">
    <div class="stat-value">10</div>
    <div class="stat-label">Years<br>in Business</div>
  </div>
  <div class="photo photo--team" role="img" aria-label="Team members in a bright office"></div>
  <div class="photo photo--towers" role="img" aria-label="Glass office towers seen from below"></div>
  <div class="photo photo--workshop" role="img" aria-label="Colleagues working on laptops around a table"></div>
  <div class="photo photo--desk" role="img" aria-label="Laptop and notes on a desk"></div>
</section>

<section class="section section--dark contact">
  <nav class="site-nav">
    <span class="brand">calvessa.</span>
    <ul class="nav-links">
      <li><a href="#">Home</a></li>
      <li><a href="#">Work</a></li>
      <li><a href="#">About</a></li>
      <li><a class="is-active" href="#">Contact</a></li>
    </ul>
  </nav>
  <h2 class="contact-title">Let’s Talk</h2>
  <a class="contact-email" href="#">info@calvessa.com</a>
  <p class="contact-pitch">Let’s build something awesome together!</p>
  <p class="contact-note">Reach out to us and we’ll get back to you.</p>
  <a class="text-link" href="#">Work with Us</a>
  <p class="footer-legal">Copyright © 2020 Calvessa. All Rights Reserved. <a href="#">Privacy Policy</a></p>
  <ul class="social-list" aria-label="Social links">
    <li><a href="#">Plaza</a></li>
    <li><a href="#">Wren</a></li>
    <li><a href="#">Nexo</a></li>
  </ul>
</section>

</body>
</html>
```